Mobile Dental Clinic for Students!!

Hi There!!
I need a marketing email to bring awareness that children need to see a dentist every year to get cleans done!! This email will be going to admin officers, principals etc.
We are a mobile dental provider, and we come to the school in our mobile van!
I have attached the flyer that will be going out to schools next week but wanted to send a marketing email as well
I have included a URL https://toothvanbookings.formlyhub.com/to/kRtPzw
to go on the marketing email to be included for easy registration for a school.
You can use stock photos~~ aswell
If you need words please copy from the flyer attached.
Also need the following on the marketing email
ph: 1800 4TEETH
www.brightpathvisits.com.au
info@brightpathvisits.com.au
Thanks and have fun with it!!!
Target Market(s)
principals, teachers, admin staff
Industry/Entity Type
Healthcare

```html
<!DOCTYPE html>
<html lang="en">
<head>
<meta charset="utf-8">
<title>BrightPath Visits – School Dental Visits</title>
<link rel="stylesheet" href="https://fonts.googleapis.com/css2?family=Montserrat:wght@400;500;600;700&family=Open+Sans:ital,wght@0,400;0,600;1,400&display=swap">
<style>
  :root {
    --page-bg: #eeeeee;
    --card-bg: #ffffff;
    --teal: #16a38b;
    --orange: #f07a22;
    --btn-orange: #f7931e;
    --btn-orange-edge: #c8740f;
    --grey-text: #8f8f8f;
    --grey-line: #c9c9c9;
    --dark-text: #333333;
    --link: #1f3f8f;
  }
  * { box-sizing: border-box; margin: 0; padding: 0; }
  html, body { width: 777px; height: 1200px; overflow: hidden; background: var(--page-bg); }
  body { font-family: "Montserrat", sans-serif; color: var(--dark-text); }

  .email { width: 528px; margin: 0 auto; position: relative; }

  .topbar { height: 32px; padding-top: 10px; display: flex; justify-content: space-between; align-items: center; }
  .browser-link { font-family: "Open Sans", sans-serif; font-size: 10px; color: var(--grey-text); text-decoration: underline; display: flex; align-items: center; gap: 6px; }
  .browser-link svg { width: 12px; height: 10px; }
  .share-group { display: flex; gap: 8px; }
  .share-btn { background: var(--btn-orange); border: 1px solid var(--btn-orange-edge); border-radius: 3px; font-family: "Open Sans", sans-serif; font-size: 10px; font-weight: 600; color: #222; padding: 3px 8px; height: 22px; display: flex; align-items: center; gap: 8px; }
  .share-btn .divider { width: 1px; height: 14px; background: var(--btn-orange-edge); }
  .share-btn .mark { width: 8px; height: 8px; background: #222; }

  .brand-row { height: 69px; display: flex; align-items: center; gap: 18px; }
  .brand-row .rule { flex: 1; height: 2px; background: #d5d5d5; }
  .brand-name { font-weight: 700; font-size: 26px; color: var(--teal); line-height: 1; letter-spacing: -0.5px; }

  .hero { height: 311px; background: var(--card-bg); border-radius: 4px 4px 0 0; display: flex; overflow: hidden; }
  .hero-photo { width: 237px; height: 100%; flex: none; background: linear-gradient(160deg, #e9d2bf 0%, #d8b08c 40%, #e56a1f 78%, #f2c81f 100%); }
  .hero-copy { flex: 1; padding-top: 111px; white-space: nowrap; }
  .hero-kicker { font-size: 21px; font-weight: 600; color: var(--teal); line-height: 1.15; }
  .hero-title { font-size: 28px; font-weight: 600; color: var(--orange); line-height: 1.2; }
  .call-btn { display: inline-block; margin-top: 8px; border: 2px solid var(--grey-line); border-radius: 4px; padding: 6px 12px; font-size: 14px; font-weight: 600; color: #666; }
  .call-btn b { color: var(--teal); font-weight: 700; }

  .offer { height: 195px; position: relative; color: #fff; text-align: center; }
  .offer-bg { position: absolute; inset: 0; }
  .offer--teal .offer-bg { background: linear-gradient(100deg, #2f9c89, #49a898 50%, #3a9a88); }
  .offer--orange .offer-bg { background: linear-gradient(100deg, #c96c3f, #e08757 50%, #d47a4c); }
  .offer--navy .offer-bg { background: linear-gradient(100deg, #3a445b, #4c5670 50%, #3f4961); }
  .offer-content { position: relative; padding-top: 26px; }
  .offer-title { font-size: 26px; font-weight: 600; line-height: 1.2; white-space: nowrap; }
  .offer-text { font-size: 16px; line-height: 1.3; margin: 10px auto 0; width: 470px; }
  .offer-btn { display: inline-block; margin-top: 14px; border: 2px solid #fff; border-radius: 4px; padding: 6px 11px; font-size: 14px; font-weight: 600; color: #fff; text-decoration: none; }

  .connect { text-align: center; padding-top: 18px; }
  .connect-title { font-family: "Open Sans", sans-serif; font-size: 17px; font-weight: 600; color: #9a9a9a; }
  .social-row { display: flex; justify-content: center; gap: 10px; margin-top: 9px; }
  .social-box { width: 34px; height: 34px; border: 2px solid #d2d2d2; border-radius: 3px; display: flex; align-items: center; justify-content: center; }
  .social-box span { width: 8px; height: 8px; background: #d2d2d2; }
  .blog-box { width: 68px; height: 34px; border: 2px solid #d2d2d2; border-radius: 3px; font-family: "Open Sans", sans-serif; font-size: 14px; font-weight: 600; color: #c2c2c2; display: flex; align-items: center; justify-content: center; }
  .copyright { font-family: "Open Sans", sans-serif; font-style: italic; font-size: 11px; color: #555; margin-top: 38px; }
  .footer-rule { height: 1px; background: #dcdcdc; margin: 30px 0 0; }
  .footer-links { text-align: center; font-family: "Open Sans", sans-serif; font-size: 10px; color: #333; margin-top: 8px; }
  .footer-links a { color: var(--link); }
</style>
</head>
<body>
<div class="email">
  <div class="topbar">
    <span class="browser-link">
      <svg viewBox="0 0 12 10"><rect x="0.5" y="0.5" width="11" height="7" fill="none" stroke="#8f8f8f"/><rect x="3" y="8.5" width="6" height="1.2" fill="#8f8f8f"/></svg>
      VIEW IN YOUR BROWSER
    </span>
    <div class="share-group">
      <span class="share-btn">TWEET <i class="divider"></i><i class="mark"></i></span>
      <span class="share-btn">SHARE <i class="divider"></i><i class="mark"></i></span>
    </div>
  </div>

  <div class="brand-row">
    <span class="rule"></span>
    <span class="brand-name">BrightPath Visits</span>
    <span class="rule"></span>
  </div>

  <section class="hero">
    <div class="hero-photo" role="img" aria-label="Photo of a smiling young boy in an orange and yellow shirt"></div>
    <div class="hero-copy">
      <p class="hero-kicker">Dedicated To Creating</p>
      <h1 class="hero-title">Beautiful Smiles</h1>
      <span class="call-btn"><b>Call:</b> 1800 4TEETH</span>
    </div>
  </section>

  <section class="offer offer--teal">
    <div class="offer-bg" role="img" aria-label="Teal-tinted photo of a family at the dentist"></div>
    <div class="offer-content">
      <h2 class="offer-title">Yearly Check-Ups For Every Child</h2>
      <p class="offer-text">Children need a dentist visit and a clean every year to keep their smiles healthy.</p>
      <a class="offer-btn" href="https://toothvanbookings.formlyhub.com/to/kRtPzw">Register Your School</a>
    </div>
  </section>

  <section class="offer offer--orange">
    <div class="offer-bg" role="img" aria-label="Orange-tinted photo of a dentist showing an X-ray to a family"></div>
    <div class="offer-content">
      <h2 class="offer-title">Our Dental Van Comes To You</h2>
      <p class="offer-text">We bring our mobile clinic to your school, so students get care without leaving class.</p>
      <a class="offer-btn" href="https://toothvanbookings.formlyhub.com/to/kRtPzw">Book A School Visit</a>
    </div>
  </section>

  <section class="offer offer--navy">
    <div class="offer-bg" role="img" aria-label="Navy-tinted photo of a child in a dental chair during a check-up"></div>
    <div class="offer-content">
      <h2 class="offer-title">Easy Registration For Schools</h2>
      <p class="offer-text">Visit www.brightpathvisits.com.au or email info@brightpathvisits.com.au</p>
      <a class="offer-btn" href="https://toothvanbookings.formlyhub.com/to/kRtPzw">Register Online Today</a>
    </div>
  </section>

  <footer class="connect">
    <p class="connect-title">Connect with us:</p>
    <div class="social-row">
      <span class="social-box" aria-label="Social link"><span></span></span>
      <span class="social-box" aria-label="Social link"><span></span></span>
      <span class="social-box" aria-label="Social link"><span></span></span>
      <span class="social-box" aria-label="Social link"><span></span></span>
      <span class="blog-box">Blog</span>
    </div>
    <p class="copyright">Copyright 2016 BrightPath Visits. All Rights Reserved</p>
    <div class="footer-rule"></div>
    <p class="footer-links"><a href="#">unsubscribe</a> | <a href="#">preferences</a></p>
  </footer>
</div>
</body>
</html>
```